Veltharion Email Direct Marketing Campaign

This is an email campaign. The copy is attached. Also attached is our logo and business card. You can get some design ideas from those and our website (www.veltharion-example.com). But don't let those limit your ideas. We are open to suggestions. We want a great looking campaign that is in line with current clean design trends (including flat design) and marketing messaging.
Updates

Hi Designers. This is not a home page design or a logo redesign. This is the design of an email campaign which will arrive in people's inboxes as a promotion. Do not take wording from the website. All wording is in the text PDF attached. No coding is required. Thanks

Industry/Entity Type

Marketing

```html
<!DOCTYPE html>
<html lang="en">
<head>
<meta charset="utf-8">
<title>Veltharion – Let us help your business</title>
<link href="https://fonts.googleapis.com/css2?family=Lato:wght@300;400;700;900&display=swap" rel="stylesheet">
<style>
  :root {
    --page-bg: #dde1e4;
    --card-bg: #ffffff;
    --brand-blue: #0b5aa8;
    --link-blue: #1b78c9;
    --accent-orange: #ec7a2c;
    --accent-pink: #db1b58;
    --accent-blue: #1b86df;
    --hero-dark: #1c1d20;
    --text-grey: #8a8a8a;
    --text-mid: #7b7b7b;
    --rule: #e4e4e4;
    --white: #ffffff;
  }
  * { box-sizing: border-box; margin: 0; padding: 0; }
  html, body {
    width: 734px; height: 1200px; overflow: hidden;
    background: var(--page-bg);
    font-family: "Lato", Arial, sans-serif;
  }
  .email-card {
    position: absolute; left: 92px; top: 37px;
    width: 550px; height: 1125px;
    background: var(--card-bg);
  }
  .masthead { position: relative; height: 92px; }
  .brand-name {
    position: absolute; left: 37px; top: 28px;
    font-size: 38px; font-weight: 900; letter-spacing: -0.5px;
    color: var(--brand-blue); line-height: 1;
  }
  .masthead-call {
    position: absolute; right: 37px; top: 79px; transform: translateY(-50%);
    margin-top: -37px;
    font-size: 16px; color: var(--brand-blue);
  }
  .hero {
    position: relative; height: 475px; width: 550px;
    clip-path: polygon(0 0, 100% 0, 100% 100%, 0 86.3%);
  }
  .hero-backdrop {
    position: absolute; inset: 0;
    background:
      radial-gradient(ellipse at 50% 0%, #56595e 0%, rgba(40,42,46,0) 60%),
      radial-gradient(ellipse at 70% 80%, rgba(30,70,140,.55) 0%, rgba(20,30,60,0) 60%),
      linear-gradient(180deg, #3a3c40 0%, var(--hero-dark) 100%);
  }
  .hero-title {
    position: absolute; top: 50px; left: 0; width: 100%;
    text-align: center; color: var(--white);
    font-size: 35px; font-weight: 400;
  }
  .promise {
    position: absolute; display: flex; align-items: center;
    color: var(--white); font-size: 26px; font-weight: 300; white-space: nowrap;
  }
  .promise strong { font-weight: 400; margin-right: 7px; }
  .promise--build { left: 18px; top: 132px; width: 312px; height: 81px; padding-left: 34px; background: var(--accent-orange); opacity: .96; }
  .promise--engage { left: 132px; top: 203px; width: 404px; height: 92px; padding-left: 36px; background: var(--accent-pink); opacity: .94; }
  .promise--found { left: 73px; top: 281px; width: 312px; height: 53px; padding-left: 40px; background: var(--accent-blue); opacity: .95; }
  .hero-button {
    position: absolute; left: 328px; top: 361px; width: 195px; height: 44px;
    border: 1px solid var(--white); border-radius: 4px;
    display: flex; align-items: center; justify-content: center;
    color: var(--white); font-size: 20px; text-decoration: none;
  }
  .about { position: absolute; left: 37px; top: 550px; width: 477px; }
  .about-heading { font-size: 20px; font-weight: 700; color: var(--brand-blue); }
  .about-intro { margin-top: 17px; font-size: 15.5px; font-weight: 300; line-height: 21px; color: var(--text-grey); }
  .benefits { list-style: none; margin-top: 12px; }
  .benefit {
    display: flex; align-items: center; height: 60px;
    border-bottom: 1px solid var(--rule);
    font-size: 15.5px; color: var(--text-mid);
  }
  .benefit svg { width: 30px; height: 30px; margin-right: 19px; flex: none; }
  .tagline {
    position: absolute; top: 900px; left: 0; width: 100%;
    text-align: center; font-size: 25px; font-weight: 300; color: var(--text-grey);
  }
  .contact-lead {
    position: absolute; top: 981px; left: 0; width: 100%;
    text-align: center; font-size: 19px; color: var(--link-blue);
  }
  .contact-row {
    position: absolute; left: 37px; top: 1015px; width: 477px; height: 46px;
    border-top: 1px solid var(--rule); border-bottom: 1px solid var(--rule);
    display: flex; align-items: center; justify-content: space-between;
    font-size: 17px; font-weight: 300; color: var(--text-grey);
  }
  .contact-item { display: flex; align-items: center; gap: 8px; white-space: nowrap; }
  .contact-item svg { flex: none; }
  .contact-email { font-size: 16px; }
  .website {
    position: absolute; top: 1077px; left: 0; width: 100%;
    text-align: center; font-size: 16.5px; font-weight: 300; color: var(--text-grey);
  }
</style>
</head>
<body>
  <main class="email-card">
    <header class="masthead">
      <div class="brand-name">Veltharion</div>
      <div class="masthead-call">Call 1300 555 019</div>
    </header>

    <section class="hero">
      <div class="hero-backdrop" role="img" aria-label="Dark background with faint blue and white engineering drawings of machine parts"></div>
      <h1 class="hero-title">Let us help your business</h1>
      <div class="promise promise--build"><strong>Build</strong> a great website</div>
      <div class="promise promise--engage"><strong>Engage</strong> with your customers</div>
      <div class="promise promise--found"><strong>Be found</strong> on Searchly</div>
      <a class="hero-button" href="#">Find out more</a>
    </section>

    <section class="about">
      <h2 class="about-heading">Veltharion</h2>
      <p class="about-intro">Veltharion is an Australian online marketing specialist for small and medium industrial businesses. That means:</p>
      <ul class="benefits">
        <li class="benefit">
          <svg viewBox="0 0 30 30"><circle cx="15" cy="15" r="13.5" fill="none" stroke="#1b78c9" stroke-width="2"/><path d="M9.5 15.5l4 4.5 7-10" fill="none" stroke="#1b78c9" stroke-width="2" stroke-linecap="round" stroke-linejoin="round"/></svg>
          We do all the work right here in Australia
        </li>
        <li class="benefit">
          <svg viewBox="0 0 30 30"><circle cx="15" cy="15" r="13.5" fill="none" stroke="#1b78c9" stroke-width="2"/><path d="M9.5 15.5l4 4.5 7-10" fill="none" stroke="#1b78c9" stroke-width="2" stroke-linecap="round" stroke-linejoin="round"/></svg>
          We keep the costs down
        </li>
        <li class="benefit">
          <svg viewBox="0 0 30 30"><circle cx="15" cy="15" r="13.5" fill="none" stroke="#1b78c9" stroke-width="2"/><path d="M9.5 15.5l4 4.5 7-10" fill="none" stroke="#1b78c9" stroke-width="2" stroke-linecap="round" stroke-linejoin="round"/></svg>
          We understand industrial markets
        </li>
      </ul>
    </section>

    <p class="tagline">Your trusted partner now and in the future</p>
    <p class="contact-lead">Get in touch to have a chat</p>

    <div class="contact-row">
      <span class="contact-item">
        <svg width="28" height="28" viewBox="0 0 28 28"><path d="M7 3l4 5-2.5 3c1.5 3.5 4 6 7.5 7.5l3-2.5 5 4-2.5 4c-9 0-18-9-18-18z" fill="none" stroke="#1b78c9" stroke-width="1.8" stroke-linejoin="round"/></svg>
        1300 555 019
      </span>
      <span class="contact-item contact-email">
        <svg width="30" height="22" viewBox="0 0 30 22"><rect x="1" y="1" width="28" height="20" fill="none" stroke="#1b78c9" stroke-width="1.8"/><path d="M1 1l14 11L29 1M1 21l10-9M29 21l-10-9" fill="none" stroke="#1b78c9" stroke-width="1.8"/></svg>
        web-services@veltharion-example.com
      </span>
    </div>

    <p class="website">www.veltharion-example.com</p>
  </main>
</body>
</html>
```